Design a New Tennis and Athletic Club- Business cards desired with a wow factor.

Help us find a exciting and useful design for our business.
1. Design should be two-sided made of materials that will last.
2. Eye-popping graphics
3. Space for changeable quotes on the back of our card with our "wolf" program logo.
4. Recolor wolf to match club colors

Target Market(s)

Players parents coaches clients

Industry/Entity Type

Business

Contact Information for Business Card

Birchwood Paddle + Wellness
Derek Hollins
Director of Tennis Operations
2817 Meadowcrest Ave NE
Grand Rapids Michigan 49318
Office (616) 555-0142
Cell (269) 555-0186
Email dhollins482@mailbox-example.com
Website http://www.bwpaddle-example.com
Facebook https://www.facebook.com/BWPaddleExample

Font styles to use
Serif

Colors
0555a3
f37122
ffffff

Requirements
Must have
• 1.interesting contemporary design,
• 2. 2 sided
• 3. ability to swap out staff information for other trainers and professionals
Nice to have
• 1.Space for changeable quotes on the back of the card
• 2. change wolf logo body to match club color blue
• 3. some white space on card for notes to be written.
Should not have
• boring same old consruction

```html
<!DOCTYPE html>
<html lang="en">
<head>
<meta charset="utf-8">
<title>Birchwood Paddle + Wellness – Business Card</title>
<link rel="stylesheet" href="https://fonts.googleapis.com/css2?family=Open+Sans:wght@400;600;700&display=swap">
<style>
  :root {
    --navy: #1b1d48;
    --navy-deep: #12143a;
    --orange: #e2552a;
    --white: #ffffff;
    --paper: #f7f7f6;
    --ink-grey: #5a5a5e;
    --rule-grey: #b9b9bd;
    --badge-blue: #3d8fd6;
    --backdrop: #d9d9dc;
  }
  * { box-sizing: border-box; margin: 0; padding: 0; }
  html, body {
    width: 1200px; height: 960px; overflow: hidden;
    background: var(--backdrop);
    font-family: "Open Sans", Arial, sans-serif;
  }
  .canvas {
    position: relative; width: 1200px; height: 960px;
  }
  .card {
    position: absolute; left: 250px; width: 700px; height: 400px;
    box-shadow: 0 10px 28px rgba(0,0,0,0.22);
    overflow: hidden;
  }

  /* Back side */
  .card-back {
    top: 40px;
    background: linear-gradient(135deg, var(--navy) 0%, var(--navy-deep) 100%);
    color: var(--white);
  }
  .program-badge {
    position: absolute; top: 26px; right: 30px;
    width: 62px; height: 50px; background: var(--badge-blue);
  }
  .back-brand {
    position: absolute; left: 0; right: 0; top: 150px;
    display: flex; align-items: center; justify-content: center; gap: 14px;
    font-size: 30px; font-weight: 600; letter-spacing: 0.5px; color: var(--white);
  }
  .brand-dot {
    width: 16px; height: 16px; border-radius: 50%; background: var(--orange);
  }
  .back-web {
    position: absolute; left: 0; right: 0; bottom: 60px; text-align: center;
    font-size: 17px; letter-spacing: 5px; color: rgba(255,255,255,0.85);
  }

  /* Front side */
  .card-front {
    top: 520px; background: var(--paper); color: var(--navy);
  }
  .front-brand {
    position: absolute; top: 90px; right: 44px;
    display: flex; align-items: center; gap: 10px;
    font-size: 22px; font-weight: 600; color: var(--navy);
  }
  .front-brand .brand-dot { width: 12px; height: 12px; }
  .staff {
    position: absolute; left: 44px; top: 142px;
  }
  .staff-name {
    font-size: 21px; font-weight: 700; letter-spacing: 0.3px; color: var(--navy-deep);
  }
  .staff-title {
    font-size: 15px; color: var(--orange); margin-top: -2px;
  }
  .divider {
    position: absolute; left: 44px; right: 44px; top: 200px;
    height: 1px; background: var(--rule-grey);
  }
  .contacts {
    position: absolute; left: 44px; top: 212px; list-style: none;
    font-size: 14.5px; line-height: 22px; color: var(--navy-deep);
  }
  .contacts li { display: flex; align-items: center; gap: 9px; }
  .contacts svg { width: 13px; height: 13px; flex: none; }
  .address {
    position: absolute; right: 44px; top: 262px; text-align: right;
    font-size: 16px; line-height: 22px; color: var(--ink-grey);
  }
  .band {
    position: absolute; bottom: 0; height: 14px;
  }
  .band-navy { left: 0; width: 46%; background: var(--navy); }
  .band-orange { right: 0; width: 54%; background: var(--orange); }
</style>
</head>
<body>
<main class="canvas">

  <section class="card card-back" aria-label="Card back">
    <div class="program-badge" role="img" aria-label="Program badge"></div>
    <div class="back-brand"><span class="brand-dot"></span><span>Birchwood Paddle + Wellness</span></div>
    <p class="back-web">www.bwpaddle-example.com</p>
  </section>

  <section class="card card-front" aria-label="Card front">
    <div class="front-brand"><span class="brand-dot"></span><span>Birchwood Paddle + Wellness</span></div>

    <div class="staff">
      <p class="staff-name">DEREK HOLLINS</p>
      <p class="staff-title">Director of Tennis Operations</p>
    </div>

    <div class="divider"></div>

    <ul class="contacts">
      <li>
        <svg viewBox="0 0 16 16" aria-hidden="true"><path fill="#12143a" d="M3 1h3l1.5 4-2 1.2a9 9 0 0 0 4.3 4.3L11 8.5l4 1.5v3a2 2 0 0 1-2 2A13 13 0 0 1 1 3a2 2 0 0 1 2-2z"/></svg>
        616 555-0142
      </li>
      <li>
        <svg viewBox="0 0 16 16" aria-hidden="true"><rect x="4" y="1" width="8" height="14" rx="1.5" fill="#12143a"/><rect x="5.5" y="3" width="5" height="8" fill="#f7f7f6"/></svg>
        269 555-0186
      </li>
      <li>
        <svg viewBox="0 0 16 16" aria-hidden="true"><rect x="1" y="1" width="14" height="14" rx="2" fill="#12143a"/></svg>
        /BWPaddleExample
      </li>
      <li>
        <svg viewBox="0 0 16 16" aria-hidden="true"><rect x="1" y="1" width="14" height="14" rx="2" fill="#12143a"/></svg>
        bwpaddle-example.com
      </li>
    </ul>

    <address class="address" style="font-style:normal">
      2817 Meadowcrest Ave NE<br>
      Grand Rapids Michigan 49318<br>
      www.bwpaddle-example.com
    </address>

    <div class="band band-navy"></div>
    <div class="band band-orange"></div>
  </section>

</main>
</body>
</html>
```